I want to revise my business card design and get a more modern and up to date design.

Brolvane Handyman Sevices originated from a family-owned and operated contractor business, performing home renovation, addition, and construction work in the NYC area since 2004. Today, we specialize in reliable and affordable handyman services for residential and commercial clients In 2014, we expanded to northern New Jersey. In 2016, we brought quality home improvement and repair services to new Bucks County, PA, and nearby New Jersey areas.
Target Market(s)
Home owners and business that might be looking for a General contractor, handyman, cleaning services and Home maintenance and property.
Industry/Entity Type
Construction Company
Contact Information for Business Card
I am open to new ideas
Colors
Designer to choose colors to be used in the design.
Look and feel
Each slider illustrates characteristics of the customer's brand and the style your logo design should communicate.

```html
<!DOCTYPE html>
<html lang="en">
<head>
<meta charset="utf-8">
<title>Brolvane Handyman Sevices – Business Cards</title>
<link href="https://fonts.googleapis.com/css2?family=Lato:wght@400;700;900&display=swap" rel="stylesheet">
<style>
  :root {
    --page-bg: #121212;
    --card-bg: #222222;
    --card-bg-back: #1d1d1d;
    --brand-red: #e3202a;
    --text-white: #f2f2f2;
  }
  * { margin: 0; padding: 0; box-sizing: border-box; }
  html, body {
    width: 1200px; height: 912px; overflow: hidden;
    background: var(--page-bg);
    font-family: "Lato", Arial, sans-serif;
  }
  .canvas { position: relative; width: 1200px; height: 912px; }
  .card {
    position: absolute; left: 270px; width: 660px; height: 377px;
    overflow: hidden;
    box-shadow: 0 18px 40px rgba(0,0,0,.6);
  }
  .card--front { top: 50px; background: var(--card-bg); }
  .card--back { top: 480px; background: var(--card-bg-back); }

  .brand { display: flex; align-items: center; gap: 16px; }
  .brand__square { width: 58px; height: 58px; background: var(--brand-red); flex: none; }
  .brand__text { display: flex; flex-direction: column; }
  .brand__name {
    font-weight: 900; font-size: 62px; line-height: 1; color: var(--text-white);
    letter-spacing: -1px;
  }
  .brand__tagline {
    font-weight: 400; font-size: 13px; letter-spacing: 5px; color: var(--text-white);
    margin-top: 6px; text-transform: uppercase; white-space: nowrap;
  }

  .card--front .brand { position: absolute; left: 150px; top: 100px; }
  .services {
    position: absolute; left: 0; right: 0; top: 232px;
    text-align: center; color: var(--text-white); font-size: 17px;
    line-height: 1.55; text-transform: uppercase; letter-spacing: .2px;
  }
  .services__dot { color: var(--brand-red); font-size: 20px; margin: 0 4px; }

  .card--back .brand { position: absolute; left: 40px; top: 155px; gap: 14px; }
  .card--back .brand__name { font-size: 48px; }
  .card--back .brand__square { width: 44px; height: 44px; }
  .card--back .brand__tagline { font-size: 10px; letter-spacing: 3.5px; }
  .divider {
    position: absolute; left: 318px; top: 120px; width: 2px; height: 136px;
    background: var(--brand-red);
  }
  .contact { position: absolute; left: 340px; top: 128px; width: 300px; color: var(--text-white); }
  .contact__name {
    font-weight: 700; font-size: 26px; color: var(--brand-red); margin-bottom: 14px;
    white-space: nowrap;
  }
  .contact__row {
    display: flex; align-items: center; gap: 9px; font-size: 16px; margin-bottom: 8px;
    white-space: nowrap;
  }
  .contact__icon { width: 15px; height: 15px; flex: none; }
</style>
</head>
<body>
<main class="canvas">
  <section class="card card--front" aria-label="Business card front">
    <div class="brand">
      <span class="brand__square"></span>
      <div class="brand__text">
        <span class="brand__name">brolvane</span>
        <span class="brand__tagline">Handyman Services</span>
      </div>
    </div>
    <p class="services">
      General Contractor<span class="services__dot">•</span>Handyman<br>
      Cleaning Services<span class="services__dot">•</span>Home Maintenance and Property
    </p>
  </section>

  <section class="card card--back" aria-label="Business card back">
    <div class="brand">
      <span class="brand__square"></span>
      <div class="brand__text">
        <span class="brand__name">brolvane</span>
        <span class="brand__tagline">Handyman Services</span>
      </div>
    </div>
    <span class="divider"></span>
    <div class="contact">
      <p class="contact__name">Marco Duarte</p>
      <p class="contact__row">
        <svg class="contact__icon" viewBox="0 0 16 16" aria-hidden="true">
          <path d="M3.5 1.5l2.5 0 1 3.5-1.7 1.2a8 8 0 0 0 4.5 4.5L11 9l3.5 1v2.5a1.5 1.5 0 0 1-1.6 1.5A12 12 0 0 1 2 3.1 1.5 1.5 0 0 1 3.5 1.5z" fill="var(--brand-red)"/>
        </svg>
        (215) 555-0147
      </p>
      <p class="contact__row">
        <svg class="contact__icon" viewBox="0 0 16 16" aria-hidden="true">
          <rect x="1" y="3" width="14" height="10" fill="var(--brand-red)"/>
          <path d="M1 3l7 6 7-6" fill="none" stroke="var(--card-bg-back)" stroke-width="1.4"/>
        </svg>
        brolvanehandyman@mailbox.com
      </p>
    </div>
  </section>
</main>
</body>
</html>
```